Web Design for Cedarfield Yard Crew

Cedarfield Yard Crew needs the photoshop files for a simple, clean and professional web design. I need a home and subpage design, although they can be very similar. See pagestridelab.com for a desired layout, although I'd like to see more design than shown on that site. The goal of the site is to attract both lawn maintenance/landscape customers and build a partner network of consultants that serve the US market. The following are needed:

- home and subpage design
- page: Home, Services, Locations, Consultants, FAQ, Contact
- if subpages have header photo, need to include 5 different header photos for each page
- favicon
Updates

I'll award the design based on the homepage concept. The minor subpage changes and other elements can be worked out in the workroom stage. Thanks, Reid

Industry/Entity Type

It Professional

```html
<!DOCTYPE html>
<html lang="en">
<head>
<meta charset="utf-8">
<title>Cedarfield Yard Crew</title>
<link href="https://fonts.googleapis.com/css2?family=Lato:ital,wght@0,300;0,400;0,700;0,900;1,400&family=Lora:ital@1&display=swap" rel="stylesheet">
<style>
:root{
  --green:#7ab648;
  --green-dark:#5f9a33;
  --green-panel:rgba(112,182,64,.88);
  --text:#555;
  --heading:#333;
  --nav:#333;
  --orange:#f08a1c;
  --orange-dark:#e27510;
  --border:#dcdcdc;
  --bg:#f2f2f2;
  --white:#fff;
  --social:#4a4a4a;
}
*{margin:0;padding:0;box-sizing:border-box}
html,body{width:1081px;height:1200px;overflow:hidden;background:var(--bg)}
body{font-family:'Lato',sans-serif;color:var(--text)}
.stage{position:absolute;left:0;top:0;width:1234px;height:1370px;transform:scale(.876);transform-origin:0 0}
.page{position:absolute;left:137px;top:37px;width:960px;height:1288px;background:var(--white);box-shadow:0 0 6px rgba(0,0,0,.12)}
.abs{position:absolute}

/* header */
.brand{left:30px;top:25px;display:flex;align-items:center;gap:14px;max-width:390px}
.brand-mark{width:52px;height:48px;border:4px solid #555;border-radius:6px;flex:none}
.brand-name{font-size:22px;font-weight:400;color:#555;letter-spacing:.5px;text-transform:uppercase;white-space:nowrap}
.callus{left:607px;top:23px;font-size:14px;font-weight:700;color:#666}
.callus span{color:var(--green);font-weight:700;margin-left:4px}
.social{display:flex;gap:6px}
.social i{display:block;width:30px;height:30px;border-radius:50%;background:var(--social)}
.social-top{left:792px;top:16px}
.nav{right:30px;top:61px;display:flex;font-size:12px;font-weight:700;color:var(--nav);text-transform:uppercase}
.nav a{color:inherit;text-decoration:none;padding:0 15px;border-left:1px solid #555;line-height:12px}
.nav a:first-child{border-left:0}
.nav a:last-child{padding-right:0}

/* hero */
.hero{left:0;top:96px;width:960px;height:543px;background:linear-gradient(180deg,#a8dcf5 0%,#56aee4 30%,#4f9fcf 48%,#6fb84a 62%,#3f9a2a 80%,#2f8420 100%)}
.hero-box{left:30px;top:237px;width:526px;height:261px;background:var(--green-panel);color:var(--white);padding:30px 46px}
.hero-kicker{font-size:24px;font-weight:400}
.hero-title{font-size:31px;font-weight:700;margin-top:4px}
.hero-text{font-size:14px;line-height:21px;margin-top:8px;width:420px}
.btn-outline{display:inline-block;margin-top:20px;border:1px solid rgba(255,255,255,.7);padding:7px 13px;font-size:18px;font-weight:700;color:var(--white);background:rgba(255,255,255,.06)}

/* contact */
.contact{left:581px;top:556px;width:349px;height:428px;background:var(--white);border:3px solid #e3e3e3;padding:24px 31px}
.contact h2{font-size:24px;font-weight:900;color:#222;letter-spacing:.2px}
.contact p{font-size:12.5px;font-weight:300;color:#888;line-height:16px;margin-top:4px}
.field{width:290px;height:37px;border:1px solid var(--border);margin-top:11px;padding:0 12px;display:flex;align-items:center;justify-content:space-between;font-size:14px;color:#666}
.field:first-of-type{margin-top:16px}
.field svg{width:16px;height:12px}
.btn-submit{display:inline-block;margin-top:22px;width:138px;height:35px;line-height:35px;text-align:center;background:linear-gradient(#f6a030,var(--orange-dark));color:var(--white);font-weight:700;font-size:14px;text-transform:uppercase}

/* features */
.feature{left:20px;width:530px;display:flex;gap:23px}
.feature-img{width:148px;height:148px;border:3px solid #e8e8e8;flex:none}
.img-lawn{background:linear-gradient(150deg,#7fbf48,#4e9a2e)}
.img-hand{background:linear-gradient(180deg,#2a3a1e 0%,#4f7d2c 45%,#66b83a 100%)}
.feature h3{font-size:21px;font-weight:400;color:var(--green);margin-top:8px}
.feature p{font-size:14px;line-height:21px;margin-top:2px}
.btn-small{display:inline-block;margin-top:9px;padding:4px 9px;border:1px solid var(--green-dark);background:var(--green);color:var(--white);font-size:12px;font-weight:700;border-radius:2px}

/* testimonials / about */
.section-title{font-size:25px;font-weight:400;color:var(--heading)}
.section-title span{color:var(--green)}
.testi-title{left:18px;top:1010px}
.arrows{left:491px;top:1041px;display:flex;gap:6px}
.arrows svg{width:24px;height:24px}
.avatar{left:20px;top:1053px;width:120px;height:120px;border-radius:50%;background:radial-gradient(circle at 50% 40%,#9bcf6a,#4f9a2e);border:2px solid #fff;box-shadow:0 0 0 1px #ddd}
.quote{left:155px;top:1072px;width:392px;font-family:'Lora',serif;font-style:italic;font-size:14.5px;line-height:21px;color:#555}
.quote b{color:var(--green);font-size:18px;font-weight:400}
.quote-author{right:416px;top:1137px;font-size:14px}
.quote-author span{color:var(--green);font-weight:700}
.about-title{left:585px;top:1010px}
.about-text{left:585px;top:1056px;width:345px;font-size:14px;line-height:21px}

/* footer */
.footer{left:-2px;top:1203px;width:962px;height:54px;background:var(--green);display:flex;align-items:center;justify-content:space-between;padding:0 30px 0 14px}
.footer-nav{display:flex;font-size:13px;color:var(--white);text-transform:uppercase}
.footer-nav a{color:inherit;text-decoration:none;padding:6px 16px;border-left:1px solid rgba(255,255,255,.35)}
.footer-nav a:first-child{border-left:0}
.footer .social i{background:var(--white)}
.copyright{left:0;top:1265px;width:960px;text-align:center;font-size:12px;color:#444}
</style>
</head>
<body>
<div class="stage">
<div class="page">

  <header>
    <div class="abs brand"><div class="brand-mark"></div><div class="brand-name">Cedarfield Yard Crew</div></div>
    <div class="abs callus">CALL US:<span>555-014-2276</span></div>
    <div class="abs social social-top"><i></i><i></i><i></i><i></i></div>
    <nav class="abs nav"><a>Home</a><a>Services</a><a>Locations</a><a>Consultants</a><a>FAQ</a><a>Contact</a></nav>
  </header>

  <section class="abs hero" role="img" aria-label="Man in a red cap riding a lawn mower across bright green grass under a blue sky"></section>
  <div class="abs hero-box">
    <div class="hero-kicker">Mauris malesuada bibendum</div>
    <div class="hero-title">Sed vehicula lorem nec parum</div>
    <p class="hero-text">Curabitur vel sem nibh. Cras lobortis diam eu lorem adipiscing pharetra. Nam nec nisi facilisis, pretium purus in, accumsan est. Fusce convallis pellentesque tristique.</p>
    <span class="btn-outline">Learn More</span>
  </div>

  <aside class="abs contact">
    <h2>CONTACT US NOW!</h2>
    <p>je suis vraiment happy to contact you right now and i am ready to take this out</p>
    <div class="field">Your Name</div>
    <div class="field">Email Address</div>
    <div class="field">Phone no.</div>
    <div class="field">Location/Country</div>
    <div class="field">Best Time to Call<svg viewBox="0 0 16 12"><path d="M0 0h16L8 12z" fill="#666"/></svg></div>
    <span class="btn-submit">Submit Now</span>
  </aside>

  <article class="abs feature" style="top:667px">
    <div class="feature-img img-lawn" role="img" aria-label="Lawn with shrubs and mowed stripe forming a smile, small red mower"></div>
    <div>
      <h3>100% Customer Satisfaction</h3>
      <p>Sed turpis tortor, imperdiet tincidunt consectetur at, semper vitae odio. Fusce dolor quam, rhoncus id tortor a, lobortis facilisis lacus. Aliquam erat volutpat.</p>
      <span class="btn-small">Read more</span>
    </div>
  </article>
  <article class="abs feature" style="top:833px">
    <div class="feature-img img-hand" role="img" aria-label="Hand resting gently over fresh green grass"></div>
    <div>
      <h3>100% Employee Retention</h3>
      <p>Ut convallis fringilla leo in cursus. Curabitur ac lacus sit amet tellus malesuada interdum. Nulla fringilla erat a eros dapibus commodo. Etiam a ornare urna.</p>
      <span class="btn-small">Read more</span>
    </div>
  </article>

  <h2 class="abs section-title testi-title">Clients <span>Testimonials</span></h2>
  <div class="abs arrows">
    <svg viewBox="0 0 24 24"><circle cx="12" cy="12" r="11" fill="#fff" stroke="#bcd9a4" stroke-width="1.5"/><path d="M14 7l-5 5 5 5" fill="none" stroke="#9cc77a" stroke-width="2"/></svg>
    <svg viewBox="0 0 24 24"><circle cx="12" cy="12" r="11" fill="#fff" stroke="var(--green)" stroke-width="1.5"/><path d="M10 7l5 5-5 5" fill="none" stroke="var(--green)" stroke-width="2"/></svg>
  </div>
  <div class="abs avatar" role="img" aria-label="Smiling couple sitting together on a lawn"></div>
  <blockquote class="abs quote"><b>“</b> Curabitur sit amet euismod mauris. Maecenas in congue nisl, vel consequat tortor. Suspendisse pellentesque felis quis interdum malesuada. <b>”</b></blockquote>
  <div class="abs quote-author">Dana Whitlow, <span>NORTHFIELD GROUP</span></div>

  <h2 class="abs section-title about-title">About <span>US</span></h2>
  <p class="abs about-text">Class aptent taciti sociosqu ad litora torquent conubia nostra, per inceptos himenaeos. Praesent aliquet erat vel velit gravida sodales. volutpat eu mauris in consectetur. Nulla dignissim tincidunt faucibus ligula vitae fringilla vitrina sparte.</p>

  <footer class="abs footer">
    <nav class="footer-nav"><a>Home</a><a>Services</a><a>Locations</a><a>Consultants</a><a>FAQ</a><a>Contact</a></nav>
    <div class="social"><i></i><i></i><i></i><i></i></div>
  </footer>
  <div class="abs copyright">All rights reserved by CEDARFIELD YARD CREW 2014</div>

</div>
</div>
</body>
</html>
```